Tolvane Air and Electrical Website

Simple and easy to use website for a Electrical and Air Conditioning contracting business.Use stock photosOnline contact portallogo still to be supplied

Target Market(s)

Mums and Dads who want a local contractor

Coding

Coded - Design and coding required

Number of Pages Required

2 page

Font styles to use
Sans Serif

Colors
f04a50
3276b5
33a6d7

Requirements
Must have
• Simple and easy to use
• Ph number
• 4 web address; linked to page
• 0417385926
• tolvane.com.au
• tolvaneelectrical.com.au
• tolvaneairandelectrical.com.au
• tolvaneair.com.au
Nice to have
• Split System Air Con Picture
• Electrical Pictures

```html
<!DOCTYPE html>
<html lang="en">
<head>
<meta charset="utf-8">
<title>Tolvane Air and Electrical</title>
<link href="https://fonts.googleapis.com/css2?family=Open+Sans:wght@400;600;700&family=Roboto:wght@400;500;700&display=swap" rel="stylesheet">
<style>
:root{
  --red:#f04a50;
  --blue:#3276b5;
  --sky:#33a6d7;
  --ink:#333;
  --muted:#777;
  --light:#f3f3f3;
  --dark:#1e1e1e;
}
*{box-sizing:border-box;margin:0;padding:0}
html,body{width:1200px;height:4072px;overflow:hidden}
body{font-family:"Open Sans",Arial,sans-serif;color:var(--ink);background:#fff;position:relative}
h1,h2,h3,h4,.btn,.nav a{font-family:"Roboto",Arial,sans-serif}
.btn{display:inline-block;background:var(--red);color:#fff;font-size:15px;font-weight:700;text-transform:uppercase;padding:12px 28px;box-shadow:0 4px 8px rgba(0,0,0,.25)}
.photo{position:absolute}
/* header */
.topbar{height:108px;position:relative}
.logo{position:absolute;left:70px;top:22px;font:700 62px "Roboto",sans-serif;color:var(--blue);letter-spacing:1px}
.quick{position:absolute;right:70px;top:36px;font:700 32px "Roboto",sans-serif;color:var(--red);display:flex;align-items:center;gap:14px}
.nav{height:40px;background:var(--blue);display:flex;padding-left:70px}
.nav a{color:#fff;font-size:16px;font-weight:500;text-transform:uppercase;padding:0 36px;line-height:40px;text-decoration:none}
.nav a.active{background:var(--sky)}
/* hero */
.hero{position:relative;height:612px;background:linear-gradient(120deg,#c9b8a4 0%,#e6e6e6 45%,#f4f4f4 100%)}
.hero-caption{position:absolute;left:70px;top:248px;width:480px;height:200px;background:rgba(40,40,40,.72);padding:20px 20px}
.hero-caption h1{color:#fff;font-size:50px;font-weight:500}
.hero-caption p{color:#fff;font-size:24px;line-height:1.2;margin:4px 0 22px}
.dots{position:absolute;left:70px;top:692px;display:flex;gap:10px}
.dots span{width:12px;height:12px;border-radius:50%;background:#ccc}
.dots span:first-child{background:var(--red)}
/* common headings */
.sec-title{text-align:center;font-size:38px;font-weight:700;color:var(--blue);text-transform:uppercase}
.rule{width:80px;height:3px;background:var(--red);margin:12px auto 0}
/* services */
.services{height:500px;padding-top:42px}
.svc-row{display:flex;justify-content:space-between;padding:0 70px;margin-top:36px}
.svc{width:320px;text-align:center}
.svc-icon{width:80px;height:80px;margin:0 auto}
.svc h3{color:var(--red);font-size:19px;font-weight:500;text-transform:uppercase;margin:14px 0 12px}
.svc p{font-size:14px;color:var(--muted);line-height:1.5;margin-bottom:26px}
/* welcome */
.welcome{position:relative;height:440px;margin-top:20px}
.welcome .panel{position:absolute;right:0;top:0;width:640px;height:440px}
.welcome-text{position:absolute;left:620px;top:60px;width:500px;color:#fff}
.welcome-text h2{font-size:38px;font-weight:500;text-transform:uppercase}
.welcome-text .bar{width:80px;height:3px;background:#fff;margin:10px 0 22px}
.welcome-text p{font-size:14px;line-height:1.6;margin-bottom:30px}
/* offers */
.offers{height:600px;padding-top:50px}
.offer-row{display:flex;justify-content:space-between;padding:0 70px;margin-top:36px}
.offer{width:330px;background:var(--light);text-align:center;padding-bottom:18px;position:relative}
.offer .img{height:200px}
.offer h3{color:var(--red);font-size:19px;font-weight:500;text-transform:uppercase;margin:18px 0 10px}
.offer p{font-size:14px;color:var(--muted);line-height:1.5;padding:0 24px;margin-bottom:22px}
/* testimonials */
.testimonials{position:relative;height:440px;margin-top:12px}
.testi-card{position:absolute;left:140px;top:90px;width:560px;height:260px;background:#fff;padding:26px 26px;box-shadow:0 4px 12px rgba(0,0,0,.15)}
.testi-card h2{color:var(--blue);font-size:36px;font-weight:500;text-transform:uppercase}
.testi-card .bar{width:80px;height:3px;background:var(--red);margin:8px 0 18px}
.testi-card p{font-size:14px;line-height:1.6;color:var(--muted);font-style:italic}
.testi-card .who{color:var(--red);font-size:14px;font-weight:700;margin-top:14px;text-transform:uppercase}
.arrow{position:absolute;left:90px;width:36px;height:36px;background:#fff;display:flex;align-items:center;justify-content:center}
/* blog */
.blog{height:560px;padding-top:30px}
.blog-row{display:flex;justify-content:space-between;padding:0 70px;margin-top:36px}
.post{width:330px}
.post .img{height:200px}
.post h4{color:var(--blue);font-size:15px;font-weight:700;text-transform:uppercase;line-height:1.4;margin:18px 0 10px}
.post p{font-size:14px;color:var(--muted);line-height:1.5;margin-bottom:20px}
/* contact */
.contact{position:relative;height:440px}
.contact .panel{position:absolute;right:0;top:0;width:660px;height:440px}
.form{position:absolute;left:610px;top:50px;width:520px}
.form h2{color:#fff;font-size:38px;font-weight:500;text-transform:uppercase}
.form .bar{width:80px;height:3px;background:#fff;margin:8px 0 24px}
.fields{display:grid;grid-template-columns:1fr 1fr;gap:14px 16px}
.field{height:40px;background:#fff;font-size:14px;color:#555;padding:11px 12px}
.field.wide{grid-column:1/3;height:100px}
.form .btn{float:right;margin-top:16px;padding:10px 28px}
/* footer */
.footer{height:272px;background:var(--dark);color:#ccc;display:flex;padding:40px 70px 0;gap:0;position:relative}
.fcol{width:265px}
.footer h4{color:#fff;font-size:16px;font-weight:700;text-transform:uppercase;margin-bottom:16px}
.footer li{list-style:none;font-size:14px;line-height:2}
.links{display:grid;grid-template-columns:1fr 1fr;width:200px}
.brandname{color:var(--sky);font-weight:700}
.sub{width:240px;height:36px;background:#fff;color:#666;font-size:13px;padding:9px 12px;margin-bottom:14px}
.sub-btn{background:var(--sky);color:#fff;font-size:13px;font-weight:700;padding:9px 16px;display:inline-block}
.social{display:flex;gap:14px;margin-bottom:40px}
.social span{width:22px;height:22px;border:2px solid #fff;border-radius:4px}
.copy{font-size:12px;color:#999;line-height:1.6}
</style>
</head>
<body>

<header class="topbar">
  <div class="logo">TOLVANE</div>
  <div class="quick">
    <svg width="30" height="30" viewBox="0 0 24 24"><path fill="#f04a50" d="M6.6 10.8c1.4 2.8 3.8 5.1 6.6 6.6l2.2-2.2c.3-.3.7-.4 1-.2 1.1.4 2.3.6 3.6.6.6 0 1 .4 1 1V20c0 .6-.4 1-1 1C10.6 21 3 13.4 3 4c0-.6.4-1 1-1h3.5c.6 0 1 .4 1 1 0 1.3.2 2.5.6 3.6.1.3 0 .7-.2 1l-2.3 2.2z"/></svg>
    QUICK CONTACT - 0417385926
  </div>
</header>
<nav class="nav">
  <a class="active">Home</a><a>About Us</a><a>Services</a><a>Blog</a><a>Testimonials</a><a>Careers</a><a>Contact Us</a>
</nav>

<section class="hero" role="img" aria-label="Photo of a smiling technician servicing a wall-mounted split system air conditioner">
  <div class="hero-caption">
    <h1>TOLVANE</h1>
    <p>Vestibulum ante ipsum primis in faucibus orci luctus et ultrices posuere.</p>
    <span class="btn">Contact Us</span>
  </div>
  <div class="dots"><span></span><span></span><span></span><span></span></div>
</section>

<section class="services">
  <h2 class="sec-title">Our Services</h2>
  <div class="rule"></div>
  <div class="svc-row">
    <div class="svc">
      <svg class="svc-icon" viewBox="0 0 80 80"><circle cx="40" cy="40" r="37" fill="none" stroke="#3276b5" stroke-width="2"/><circle cx="40" cy="32" r="10" fill="none" stroke="#3276b5" stroke-width="2"/><path d="M22 62c2-10 9-14 18-14s16 4 18 14" fill="none" stroke="#3276b5" stroke-width="2"/><path d="M42 50l-4 7h5l-3 7" fill="none" stroke="#f04a50" stroke-width="2"/></svg>
      <h3>Electrical Contracting</h3>
      <p>Vestibulum ante ipsum primis in faucibus orci luctus et ultrices posuere cubilia. Sed do eiusmod tempor incididunt labore.</p>
      <span class="btn">Read More</span>
    </div>
    <div class="svc">
      <svg class="svc-icon" viewBox="0 0 80 80"><rect x="12" y="24" width="56" height="20" rx="3" fill="none" stroke="#3276b5" stroke-width="2"/><line x1="18" y1="38" x2="62" y2="38" stroke="#3276b5" stroke-width="2"/><path d="M26 50v10M40 50v12M54 50v10" stroke="#f04a50" stroke-width="2" fill="none"/></svg>
      <h3>Air Conditioning</h3>
      <p>Vestibulum ante ipsum primis in faucibus orci luctus et ultrices posuere cubilia. Sed do eiusmod tempor incididunt labore.</p>
      <span class="btn">Read More</span>
    </div>
    <div class="svc">
      <svg class="svc-icon" viewBox="0 0 80 80"><circle cx="40" cy="40" r="37" fill="none" stroke="#3276b5" stroke-width="2"/><circle cx="40" cy="40" r="10" fill="none" stroke="#3276b5" stroke-width="2"/><path d="M40 20v8M40 52v8M20 40h8M52 40h8M26 26l6 6M48 48l6 6M54 26l-6 6M26 54l6-6" stroke="#f04a50" stroke-width="2"/></svg>
      <h3>Repair &amp; Maintanance</h3>
      <p>Vestibulum ante ipsum primis in faucibus orci luctus et ultrices posuere cubilia. Sed do eiusmod tempor incididunt labore.</p>
      <span class="btn">Read More</span>
    </div>
  </div>
</section>

<section class="welcome">
  <div class="photo" role="img" aria-label="Photo of a technician installing a split system air conditioner while a customer watches" style="left:0;top:0;width:620px;height:440px;background:linear-gradient(135deg,#e8e4de,#bcb2a6)"></div>
  <svg class="panel" viewBox="0 0 640 440" preserveAspectRatio="none"><polygon points="90,0 640,0 640,440 0,440" fill="#3276b5"/></svg>
  <div class="welcome-text">
    <h2>Welcome to Tolvane</h2>
    <div class="bar"></div>
    <p>Lorem ipsum dolor sit amet, consectetur adipiscing elit tellus luctus quam ac ullamcorper. Suspendisse id ligula quis arcu ultrices tincidunt. Curabitur non dapibus mauris. Integer facilisis arcu ut purus pellentesque. Sed sit amet pellentesque lorem, ut pharetra lacus. Etiam luctus libero, condimentum quam libero et accumsan imperdiet augue. Aenean mattis nisi odio at purus.</p>
    <span class="btn">Read More</span>
  </div>
</section>

<section class="offers">
  <h2 class="sec-title">Service Area Offers</h2>
  <div class="rule"></div>
  <div class="offer-row">
    <div class="offer">
      <div class="img" role="img" aria-label="Photo of a technician fitting an air conditioner in a home" style="background:linear-gradient(135deg,#d8cfc6,#9fb3c6)"></div>
      <h3>Residential</h3>
      <p>Vestibulum ante ipsum primis in faucibus orci luctus et ultrices posuere cubilia lobortis turpis in odio blandit.</p>
      <span class="btn">Read More</span>
    </div>
    <div class="offer">
      <div class="img" role="img" aria-label="Photo of a worker servicing an office air conditioner" style="background:linear-gradient(135deg,#f0eeea,#cfc9c0)"></div>
      <h3>Commercial</h3>
      <p>Vestibulum ante ipsum primis in faucibus orci luctus et ultrices posuere cubilia lobortis turpis in odio blandit.</p>
      <span class="btn">Read More</span>
    </div>
    <div class="offer">
      <div class="img" role="img" aria-label="Photo of an industrial electrical substation" style="background:linear-gradient(135deg,#6c7d94,#c9d3de)"></div>
      <h3>Industrial</h3>
      <p>Vestibulum ante ipsum primis in faucibus orci luctus et ultrices posuere cubilia lobortis turpis in odio blandit.</p>
      <span class="btn">Read More</span>
    </div>
  </div>
</section>

<section class="testimonials">
  <div class="photo" style="left:0;top:0;width:1200px;height:440px;background:var(--sky)"></div>
  <div class="photo" role="img" aria-label="Photo of a happy couple relaxing on a sofa at home" style="left:600px;top:0;width:600px;height:440px;background:linear-gradient(135deg,#8a6e52,#d9c7b2)"></div>
  <div class="arrow" style="top:180px"><svg width="14" height="14" viewBox="0 0 14 14"><path d="M10 1L4 7l6 6" stroke="#333" stroke-width="2" fill="none"/></svg></div>
  <div class="arrow" style="top:222px"><svg width="14" height="14" viewBox="0 0 14 14"><path d="M4 1l6 6-6 6" stroke="#333" stroke-width="2" fill="none"/></svg></div>
  <div class="testi-card">
    <h2>Customer Testimonials</h2>
    <div class="bar"></div>
    <p>" Lorem ipsum dolor sit amet, consectetur adipiscing elit tellus luctus quam ac ullamcorper. Suspendisse id ligula quis arcu ultrices tincidunt. Curabitur non dapibus mauris. Integer facilisis arcu ut purus pellentesque. Sed sit amet pellentesque lorem..."</p>
    <div class="who">Jamie Hartwell</div>
  </div>
</section>

<section class="blog">
  <h2 class="sec-title">Blog Posts</h2>
  <div class="rule"></div>
  <div class="blog-row">
    <div class="post">
      <div class="img" role="img" aria-label="Photo of an electrician working on a switchboard" style="background:linear-gradient(135deg,#4a5a6e,#d7c49a)"></div>
      <h4>Nam eget nulla in dolor eleifend dignissim sit amet</h4>
      <p>Curabitur non dapibus mauris. Integer facilisis arcu ut purus pellentesque tempor nisl.</p>
      <span class="btn">Read More</span>
    </div>
    <div class="post">
      <div class="img" role="img" aria-label="Photo of a technician repairing an air conditioning unit" style="background:linear-gradient(135deg,#f2f2f2,#8fa3c4)"></div>
      <h4>Nam eget nulla in dolor eleifend dignissim sit amet</h4>
      <p>Curabitur non dapibus mauris. Integer facilisis arcu ut purus pellentesque tempor nisl.</p>
      <span class="btn">Read More</span>
    </div>
    <div class="post">
      <div class="img" role="img" aria-label="Photo of a split system air conditioner on a white wall" style="background:linear-gradient(135deg,#fafafa,#cfd3d6)"></div>
      <h4>Nam eget nulla in dolor eleifend dignissim sit amet</h4>
      <p>Curabitur non dapibus mauris. Integer facilisis arcu ut purus pellentesque tempor nisl.</p>
      <span class="btn">Read More</span>
    </div>
  </div>
</section>

<section class="contact">
  <div class="photo" role="img" aria-label="Street map showing the business location" style="left:0;top:0;width:640px;height:440px;background:linear-gradient(135deg,#e9e6df,#cfe0c6)"></div>
  <svg class="panel" viewBox="0 0 660 440" preserveAspectRatio="none"><polygon points="80,0 660,0 660,440 0,440" fill="#3276b5"/></svg>
  <div class="form">
    <h2>Quick Contact</h2>
    <div class="bar"></div>
    <div class="fields">
      <div class="field">Name</div><div class="field">Phone No</div>
      <div class="field">Email Address</div><div class="field">Subject</div>
      <div class="field wide">Message</div>
    </div>
    <span class="btn">Submit</span>
  </div>
</section>

<footer class="footer">
  <div class="fcol">
    <h4>Site Map</h4>
    <ul class="links"><li>Home</li><li>Testimonials</li><li>About Us</li><li>Careers</li><li>Services</li><li>Contact Us</li><li>Blog</li></ul>
  </div>
  <div class="fcol">
    <h4>Contact Info</h4>
    <ul><li class="brandname">TOLVANE</li><li>14 Harbour Lane,</li><li>Brisbane QLD 4000</li><li>0417385926</li><li>info@tolvane.com.au</li></ul>
  </div>
  <div class="fcol" style="width:300px">
    <h4>Email Subscribing</h4>
    <div class="sub">Enter Name</div>
    <div class="sub">Enter Email Address</div>
    <span class="sub-btn">SIGN UP</span>
  </div>
  <div class="fcol">
    <h4>Follow Us</h4>
    <div class="social"><span></span><span></span><span></span><span></span><span></span></div>
    <div class="copy">Copyright © 2024 Tolvane Air and Electrical<br>All Rights Reserved</div>
  </div>
</footer>

</body>
</html>
```